Personalised Poetry business needs a business card designed

I am a writer that specialises in personalised poetry for people for significant life events.
I want a business card that stands out and portrays class and professionalism but is also welcoming & indicates warmth and honesty.
I'm happy with the logo that was designed for me, I would like to see it in raised print on the business card. I am open to suggestions on colours but think perhaps gold or silver writing for the logo would look good. I would like just the logo and my name and contact details on the front of the card. On the back of the card, I would like a list of the different events I provide poems for I will upload a photo of my current business card for reference. My current logo has a shading behind it that I don't like, I just want the words of the logo without any background colour

Target Market(s)

People wanting to provide a unique gift to someone special in their life

Industry/Entity Type

Writer

Contact Information for Business Card

Logo, my name and contact details on the front and a list of all the events I write poetry for on the back

Font styles to use
Script

Requirements
Must have
• I would like to see the logo, if possible, in a raised type of print on the card so that you can feel the actual words. I would like to have a glossy finish to the card and be able to print it on good quality board
Should not have
• The shading that is currently behind the logo on my current business card

```html
<!DOCTYPE html>
<html lang="en">
<head>
<meta charset="utf-8">
<title>Lines of Always – Business Card</title>
<link rel="stylesheet" href="https://fonts.googleapis.com/css2?family=Nunito:wght@400;600;700&family=Yellowtail&display=swap">
<style>
  :root {
    --backdrop: #000000;
    --card: #ffffff;
    --ink: #333333;
    --ink-soft: #3d3d3d;
    --gold-deep: #c68a1f;
    --gold-light: #f7efb4;
    --gold-mid: #f6d56a;
    --gold-warm: #f8c444;
    --gold-copper: #d78f4c;
    --silver-dark: #8a8a8a;
    --silver-light: #e6e6e6;
  }
  * { box-sizing: border-box; margin: 0; padding: 0; }
  html, body {
    width: 1200px; height: 1200px; overflow: hidden;
    background: var(--backdrop);
  }
  .stage { position: relative; width: 1200px; height: 1200px; }
  .card {
    position: absolute; left: 169px; width: 862px; height: 502px;
    background: var(--card); overflow: hidden;
    box-shadow: 0 6px 18px rgba(255,255,255,0.06);
  }
  .card--front { top: 69px; }
  .card--back { top: 628px; height: 503px; }

  .brand { position: absolute; text-align: center; color: var(--ink); font-family: "Nunito", sans-serif; }
  .brand__name { display: block; font-weight: 400; letter-spacing: 1px; line-height: 1; }
  .brand__tagline { display: block; font-weight: 400; }
  .brand__dot {
    display: inline-block; border-radius: 50%;
    border: 2px solid var(--ink); vertical-align: middle;
  }
  .card--front .brand { left: 0; width: 862px; top: 78px; }
  .card--front .brand__name { font-size: 64px; }
  .card--front .brand__tagline { font-size: 28px; margin-top: 18px; }
  .card--front .brand__dot { width: 22px; height: 22px; margin-top: 18px; }

  .silver-rule {
    position: absolute; left: 0; top: 331px; width: 862px; height: 12px;
    background: linear-gradient(90deg, var(--silver-light), var(--silver-dark) 20%, var(--silver-light) 50%, #b5b5b5 75%, var(--silver-light));
  }
  .gold-band {
    position: absolute; left: 0; top: 343px; width: 862px; height: 159px;
    background: linear-gradient(90deg, var(--gold-deep) 0%, #e6c062 14%, var(--gold-light) 31%, var(--gold-mid) 55%, var(--gold-warm) 82%, var(--gold-copper) 100%);
  }
  .holder {
    position: absolute; left: 81px; top: 58px;
    font-family: "Nunito", sans-serif; font-weight: 700; font-size: 36px; color: var(--ink);
  }
  .contact { position: absolute; right: 60px; top: 34px; list-style: none; font-family: "Nunito", sans-serif; font-size: 23px; color: var(--ink); }
  .contact__item { display: flex; align-items: center; justify-content: flex-end; gap: 14px; height: 34px; }
  .contact__icon { width: 18px; height: 18px; fill: var(--ink); }

  .headline {
    position: absolute; left: 0; width: 862px; top: 44px; text-align: center;
    font-family: "Yellowtail", cursive; font-size: 44px; color: var(--ink);
  }
  .card--back .brand { left: 410px; width: 390px; top: 150px; }
  .card--back .brand__name { font-size: 40px; }
  .card--back .brand__tagline { font-size: 17px; margin-top: 12px; }
  .card--back .brand__dot { width: 13px; height: 13px; margin-top: 10px; }

  .events { position: absolute; left: 60px; top: 276px; list-style: none; font-family: "Nunito", sans-serif; font-size: 23px; color: var(--ink-soft); }
  .events li { height: 33px; }
  .events li::before { content: "•"; margin-right: 8px; }
</style>
</head>
<body>
<main class="stage">
  <section class="card card--front">
    <div class="brand">
      <span class="brand__name">Lines of Always</span>
      <span class="brand__tagline">Personalised Poetry</span>
      <span class="brand__dot"></span>
    </div>
    <div class="silver-rule"></div>
    <div class="gold-band">
      <p class="holder">Marcus Hollow</p>
      <ul class="contact">
        <li class="contact__item">0400 555 120
          <svg class="contact__icon" viewBox="0 0 24 24" aria-hidden="true"><path d="M6.6 10.8a15.1 15.1 0 0 0 6.6 6.6l2.2-2.2a1 1 0 0 1 1-.25 11.4 11.4 0 0 0 3.6.57 1 1 0 0 1 1 1V20a1 1 0 0 1-1 1A17 17 0 0 1 3 4a1 1 0 0 1 1-1h3.5a1 1 0 0 1 1 1c0 1.25.2 2.45.57 3.57a1 1 0 0 1-.25 1z"/></svg>
        </li>
        <li class="contact__item">marcus@linesofalways.com
          <svg class="contact__icon" viewBox="0 0 24 24" aria-hidden="true"><path d="M2 5h20v14H2z" fill="none"/><path d="M2 5h20v14H2V5zm2 2v.4l8 5 8-5V7H4z"/></svg>
        </li>
      </ul>
    </div>
  </section>

  <section class="card card--back">
    <h1 class="headline">Monentous Life Events Personalised in Poetry</h1>
    <div class="brand">
      <span class="brand__name">Lines of Always</span>
      <span class="brand__tagline">Personalised Poetry</span>
      <span class="brand__dot"></span>
    </div>
    <ul class="events">
      <li>Weddings &amp; Anniversaries</li>
      <li>Birthdays &amp; Christmas</li>
      <li>Valentines Day</li>
      <li>Retirements, Business &amp; Corporate Events</li>
      <li>Funerals &amp; Eulogies</li>
    </ul>
  </section>
</main>
</body>
</html>
```